Quill Refrigeration. Refrigeration and air conditioning specialists.

We need a website to promote our business. We would a modern simple design using the colours from our logo and black. We want it to be fun but proffesional.

Target Market(s)

Commercial

Number of Pages Required

4 page

Requirements
Must have
• Home Page, About Us, Services and Contact Us.
• 24/7 365 days service available.
• Quill Refrigeration's dedicated team specialises in commercial refrigeration and air conditioning equipment.
• Based in Joondalup, we cover Perth Metro and surrounding areas.
Nice to have
• KNOWLEDGE . EXPERIENCE . PASSION in bold.
• Our experienced and highly trained technicians provide extensive knowledge and exceptional skills for your commercial refrigeration and air conditioning requirements.
• Pictures of commercial refrigeration.
Should not have
• No mention of domestic services.

```html
<!DOCTYPE html>
<html lang="en">
<head>
<meta charset="utf-8">
<title>Quill Refrigeration</title>
<link rel="stylesheet" href="https://fonts.googleapis.com/css2?family=Montserrat:wght@500;600;700;800&family=Open+Sans:wght@400;600&display=swap">
<style>
:root{
  --lime:#8cc63f;
  --lime-dark:#74ad2a;
  --ink:#2b2b2b;
  --muted:#8a8f96;
  --hero-bg:#eef1f5;
  --team-bg:#e6edf0;
  --footer-bg:#454545;
  --footer-deep:#3a3a3a;
  --white:#ffffff;
}
*{box-sizing:border-box;margin:0;padding:0}
html,body{width:1200px;height:2700px;overflow:hidden;background:var(--white)}
body{font-family:"Open Sans",Arial,sans-serif;color:var(--ink);position:relative}
h1,h2,h3,h4,.nav a,.btn,.brand{font-family:"Montserrat",Arial,sans-serif}
.btn{display:inline-block;background:var(--lime);color:var(--white);font-size:11px;font-weight:700;letter-spacing:.5px;padding:12px 24px;border-radius:3px;text-decoration:none}

/* header */
.site-header{position:absolute;top:0;left:0;width:1200px;height:60px;display:flex;align-items:center;padding:0 120px;background:var(--white)}
.brand{color:var(--lime);font-weight:800;font-size:19px;display:flex;align-items:center;gap:8px}
.brand .dot{width:12px;height:12px;background:var(--lime)}
.nav{display:flex;gap:30px;margin-left:110px}
.nav a{font-size:11px;font-weight:600;color:var(--ink);text-decoration:none;padding-bottom:6px}
.nav a.active{border-bottom:2px solid var(--lime)}
.header-call{margin-left:auto;display:flex;align-items:center;gap:10px}
.header-call .ico{width:28px;height:28px;border-radius:50%;background:var(--ink);display:flex;align-items:center;justify-content:center}
.header-call small{display:block;font-size:10px;color:var(--muted)}
.header-call strong{font-family:"Montserrat",sans-serif;font-size:14px}

/* hero */
.hero{position:absolute;top:60px;left:0;width:1200px;height:500px;background:var(--hero-bg);overflow:hidden}
.hero-photo{position:absolute;right:0;top:0;width:560px;height:500px;background:linear-gradient(120deg,#dfe6ee 0%,#c9d3de 45%,#8aa4c4 100%)}
.hero-copy{position:absolute;left:120px;top:118px;width:440px}
.hero-copy .eyebrow{font-size:12px;color:var(--muted);margin-bottom:8px}
.hero-copy h1{font-size:26px;font-weight:800;color:var(--ink);letter-spacing:.3px;margin-bottom:12px}
.hero-copy p{font-size:13px;line-height:1.6;color:#55595f;width:300px;margin-bottom:26px}
.hero-dots{position:absolute;left:120px;top:392px;display:flex;gap:8px}
.hero-dots span{width:7px;height:7px;border-radius:50%;background:#c3c9d0}
.hero-dots span:first-child{background:var(--lime)}
.hero-wave{position:absolute;left:0;bottom:0;width:1200px;height:70px}

/* services */
.services{position:absolute;top:600px;left:0;width:1200px;text-align:center}
.section-title{font-size:15px;font-weight:800;letter-spacing:.5px}
.section-title:after{content:"";display:block;width:40px;height:2px;background:var(--lime);margin:10px auto 0}
.services .intro{width:620px;margin:16px auto 0;font-size:11px;line-height:1.7;color:var(--muted)}
.service-card{position:absolute;top:158px;width:440px;height:280px}
.service-card .photo{width:440px;height:280px}
.service-card .caption{position:absolute;right:-20px;bottom:-14px;width:200px;background:var(--lime);color:var(--white);text-align:left;padding:16px 18px}
.service-card h3{font-size:13px;font-weight:700;line-height:1.3;margin-bottom:8px}
.service-card p{font-size:10px;line-height:1.6}
.card-one{left:130px}
.card-one .photo{background:linear-gradient(150deg,#d9dde2,#8e969f 60%,#5d6670)}
.card-two{left:630px}
.card-two .photo{background:linear-gradient(150deg,#cfd5da,#9ba4ad 55%,#6f7a84)}

/* welcome */
.welcome{position:absolute;top:1160px;left:0;width:1200px;height:400px;background:#f4f5f6}
.welcome-photo{position:absolute;left:0;top:0;width:560px;height:400px;background:linear-gradient(135deg,#b9bec3 0%,#8f969d 50%,#6b7a5a 100%)}
.welcome-copy{position:absolute;left:620px;top:52px;width:440px}
.welcome-copy h2{font-size:16px;font-weight:800;letter-spacing:.4px}
.welcome-copy h2:after{content:"";display:block;width:40px;height:2px;background:var(--lime);margin-top:10px}
.welcome-copy p{font-size:11px;line-height:1.75;color:var(--muted);margin-top:16px}
.welcome-copy .btn{margin-top:30px}

/* team */
.team{position:absolute;top:1560px;left:0;width:1200px;height:520px;background:var(--team-bg)}
.team h2{position:absolute;left:145px;top:50px;font-size:14px;font-weight:800}
.team-grid{position:absolute;left:145px;top:112px;display:flex;gap:20px}
.member{width:218px;background:var(--white)}
.member .photo{height:200px}
.member:nth-child(1) .photo{background:linear-gradient(160deg,#c7ccd2,#5f7389)}
.member:nth-child(2) .photo{background:linear-gradient(160deg,#d0c8bd,#7d7466)}
.member:nth-child(3) .photo{background:linear-gradient(160deg,#e3e4e6,#4c5158)}
.member:nth-child(4) .photo{background:linear-gradient(160deg,#cfd3c8,#9a7d4f)}
.member .info{padding:14px 16px 18px}
.member h4{font-size:10px;font-weight:700}
.member span{font-size:9px;color:var(--lime)}

/* cta */
.cta{position:absolute;top:2120px;left:0;width:1200px;text-align:center}
.cta h2{font-size:25px;font-weight:700}
.cta p{font-size:10px;color:var(--muted);margin:8px 0 18px}

/* footer */
.site-footer{position:absolute;top:2290px;left:0;width:1200px;height:410px}
.footer-wave{position:absolute;top:0;left:0;width:1200px;height:110px}
.footer-body{position:absolute;top:100px;left:0;width:1200px;height:310px;background:var(--footer-bg)}
.contacts{position:absolute;left:145px;top:78px;display:flex;gap:0}
.contact{display:flex;gap:14px;width:230px}
.contact:first-child{width:300px}
.contact svg{flex:none}
.contact h4{color:var(--white);font-size:11px;font-weight:700;margin-bottom:6px}
.contact p{color:#cfcfcf;font-size:10px;line-height:1.6}
.footer-bar{position:absolute;left:145px;right:140px;top:238px;border-top:1px solid #595959;padding-top:20px;display:flex;justify-content:space-between;align-items:center}
.footer-bar small{color:#aaa;font-size:10px}
.socials{display:flex;gap:6px}
.socials span{width:18px;height:18px;display:block}
</style>
</head>
<body>

<header class="site-header">
  <div class="brand"><span class="dot"></span>Quill Refrigeration</div>
  <nav class="nav">
    <a class="active" href="#">HOME</a><a href="#">ABOUT US</a><a href="#">SERVICES</a><a href="#">PRODUCTS</a><a href="#">CONTACT US</a>
  </nav>
  <div class="header-call">
    <span class="ico"><svg width="14" height="14" viewBox="0 0 24 24"><path fill="#fff" d="M6.6 10.8a15 15 0 006.6 6.6l2.2-2.2a1 1 0 011-.25 11.4 11.4 0 003.6.57 1 1 0 011 1V20a1 1 0 01-1 1A17 17 0 013 4a1 1 0 011-1h3.5a1 1 0 011 1c0 1.25.2 2.45.57 3.57a1 1 0 01-.25 1z"/></svg></span>
    <div><small>Call Now Free Service</small><strong>1-800-555-0142</strong></div>
  </div>
</header>

<section class="hero">
  <div class="hero-photo" role="img" aria-label="Technician in blue shirt testing an open commercial refrigerator with a multimeter"></div>
  <div class="hero-copy">
    <div class="eyebrow">Committed to top quality services</div>
    <h1>KNOWLEDGE . EXPERIENCE . PASSION</h1>
    <p>We make it a priority to offer flexible services to accommodate your needs</p>
    <a class="btn" href="#">GET A QUOTE NOW</a>
  </div>
  <div class="hero-dots"><span></span><span></span><span></span></div>
  <svg class="hero-wave" viewBox="0 0 1200 70" preserveAspectRatio="none">
    <path d="M0 40 C300 5 700 70 1200 20 L1200 70 L0 70Z" fill="var(--lime)"/>
    <path d="M0 55 C320 20 720 80 1200 38 L1200 70 L0 70Z" fill="#fff"/>
  </svg>
</section>

<section class="services">
  <h2 class="section-title">SERVICES WE OFFER</h2>
  <p class="intro">Our highly trained technicians bring extensive knowledge and exceptional skills to every commercial refrigeration and air conditioning job across Perth Metro and surrounding areas, 24/7, 365 days a year.</p>
  <article class="service-card card-one">
    <div class="photo" role="img" aria-label="Technicians in hard hats installing outdoor refrigeration condenser units"></div>
    <div class="caption"><h3>Expert Installation in Refrigeration</h3><p>From cool rooms to display cabinets, we install commercial systems built to last.</p></div>
  </article>
  <article class="service-card card-two">
    <div class="photo" role="img" aria-label="Technician in hard hat servicing an air conditioning unit"></div>
    <div class="caption"><h3>Air conditioning Design &amp; Installation</h3><p>We design efficient air conditioning solutions that keep your business running.</p></div>
  </article>
</section>

<section class="welcome">
  <div class="welcome-photo" role="img" aria-label="Technician kneeling beside an outdoor air conditioning condenser unit"></div>
  <div class="welcome-copy">
    <h2>WELCOME TO QUILL REFRIGERATION</h2>
    <p>Quill Refrigeration's dedicated team specialises in commercial refrigeration and air conditioning equipment. Based in Joondalup, we cover Perth Metro and surrounding areas.</p>
    <p>Our experienced and highly trained technicians provide extensive knowledge and exceptional skills for your commercial refrigeration and air conditioning requirements.</p>
    <p>With service available 24/7, 365 days a year, we are ready whenever your business needs us most.</p>
    <a class="btn" href="#">MORE DETAILS</a>
  </div>
</section>

<section class="team">
  <h2>MEET THE TEAM</h2>
  <div class="team-grid">
    <div class="member"><div class="photo" role="img" aria-label="Team member portrait"></div><div class="info"><h4>DANIEL MARSH</h4><span>Managing Director</span></div></div>
    <div class="member"><div class="photo" role="img" aria-label="Team member portrait"></div><div class="info"><h4>LIAM PORTER</h4><span>Senior Technician</span></div></div>
    <div class="member"><div class="photo" role="img" aria-label="Team member portrait"></div><div class="info"><h4>OWEN FLETCHER</h4><span>Service Technician</span></div></div>
    <div class="member"><div class="photo" role="img" aria-label="Team member portrait"></div><div class="info"><h4>RYAN CALDWELL</h4><span>Installation Lead</span></div></div>
  </div>
</section>

<section class="cta">
  <h2>Quality heating &amp; air conditioning solutions</h2>
  <p>Reliable commercial service across Perth Metro, available around the clock</p>
  <a class="btn" href="#">CONTACT US</a>
</section>

<footer class="site-footer">
  <svg class="footer-wave" viewBox="0 0 1200 110" preserveAspectRatio="none">
    <path d="M0 60 C280 10 560 20 820 55 C980 78 1100 70 1200 40 L1200 110 L0 110Z" fill="var(--lime)"/>
    <path d="M0 78 C300 30 580 40 840 72 C1000 92 1110 86 1200 60 L1200 110 L0 110Z" fill="var(--footer-bg)"/>
  </svg>
  <div class="footer-body">
    <div class="contacts">
      <div class="contact">
        <svg width="18" height="22" viewBox="0 0 24 30"><path fill="var(--lime)" d="M12 0a10 10 0 00-10 10c0 7.5 10 20 10 20s10-12.5 10-20A10 10 0 0012 0zm0 14a4 4 0 110-8 4 4 0 010 8z"/></svg>
        <div><h4>ADDRESS</h4><p>Quill Refrigeration<br>18 Harbour Lane, Joondalup<br>Western Australia 6027</p></div>
      </div>
      <div class="contact">
        <svg width="18" height="18" viewBox="0 0 24 24"><path fill="var(--lime)" d="M6.6 10.8a15 15 0 006.6 6.6l2.2-2.2a1 1 0 011-.25 11.4 11.4 0 003.6.57 1 1 0 011 1V20a1 1 0 01-1 1A17 17 0 013 4a1 1 0 011-1h3.5a1 1 0 011 1c0 1.25.2 2.45.57 3.57a1 1 0 01-.25 1z"/></svg>
        <div><h4>CALL</h4><p>08 6100 2741</p></div>
      </div>
      <div class="contact">
        <svg width="18" height="18" viewBox="0 0 24 24"><path fill="var(--lime)" d="M6 2h12v6H6zM3 9h18v9h-3v4H6v-4H3zm5 6v5h8v-5z"/></svg>
        <div><h4>FAX</h4><p>08 6100 2742</p></div>
      </div>
      <div class="contact">
        <svg width="20" height="16" viewBox="0 0 24 18"><path fill="var(--lime)" d="M0 0h24v18H0zm2 2v.5l10 7 10-7V2zm0 3v11h20V5l-10 7z"/></svg>
        <div><h4>EMAIL</h4><p>hello@quillrefrigeration.example</p></div>
      </div>
    </div>
    <div class="footer-bar">
      <small>Quill Refrigeration © 2024 . All Rights Reserved</small>
      <div class="socials">
        <span style="background:#3b8fd6"></span><span style="background:#4aa3df"></span><span style="background:#8cc63f"></span><span style="background:#e0663a"></span><span style="background:#d84a3a"></span><span style="background:#7a7a7a"></span>
      </div>
    </div>
  </div>
</footer>

</body>
</html>
```